Label Sticker Design for Apothecary Brand

Hello! We are an independent grassroots business located in Ontario, Canada that specializes in making organic botanical and herbal skin care, tea, witchcraft and wellness products. We have been in business for 5 years and are looking to create a label sticker with one of our slogans for use in packaging.

Our brand is dark, herbal, witchy, and modern with old-world apothecary and vintage influences. We want a label that will be VERY clean, and easily explain what our product is, while conveying a sense of mysticism and magic, as well as a traditional apothecary vibe.

We have attached design inspiration to give you an idea of the style that we would like. Our demographic is hipster, current, (think finger tattoos, linen dresses, and organic groceries), and they care deeply about where we source our ingredients, and how we craft our product. We don't want an old-school sticker that looks like it should be on the shelves of a health food store. The design should be contemporary, upmarket, modern and clean, but evoke a strong sense of magic and self-care with wild gathered herbs and unusual wild flowers!

This will be used as a packaging sticker for our shipping boxes.

We look forward to your winning design!
Thank you very much.

Target Market(s)

20 - 50yr Female Demographic
Natural, bohemian, earthy, hipster and modern

Key Words: Minimalist Tattoos, Organic Skin Care, Bohemian, Witchy, Dark, Moody, Confident, Sustainable, Ethical,

PLEASE VIEW PHOTOS BEFORE SUBMITTING A DESIGN ;)

Industry/Entity Type

Skin Care Product

Font styles to use
Serif
Script

Colors
1b1b1b
5c5c5c
fbfbfb

Requirements
Must have
• Clean and Simple - Take a look at the photos we've posted!
• Black / greyscale (No color)
• Label sticker must be a rectangle (3" x 2")
• Very Modern with a touch of old-world
• We are open to a variety of font styles. Please see photo FONT in image files, or the images 'Bottle Inspiration'
• Please use the following text:
• Hollow Vesperine
• --------------------
• Crafted with Magic
• * Once your design is chosen and purchased, we will require the names of all fonts and sources of imagery used.
Nice to have
• A moody botanical graphic surrounding the text. Tangled wild, antique botanical illustrations. Not mandatory, but would be very nice.
Should not have
• Colour
• Messy or overly dramatic fonts
• Cartoon Imagery
• Leaf Motif
• Female Body Silhouettes
• Scroll or decorative borders.
• Butterflies, birds etc
• Actual pictures of witches
• Mandalas or Messy Graphics

```html
<!DOCTYPE html>
<html lang="en">
<head>
<meta charset="UTF-8">
<title>Hollow Vesperine Label Set</title>
<link rel="stylesheet" href="https://fonts.googleapis.com/css2?family=Allura&family=Crimson+Text:ital@0;1&display=swap">
<style>
  :root {
    --canvas: #ffffff;
    --label-ink: #1b1b1b;
    --label-edge: #2a2a2a;
    --label-glow: #333333;
    --sprig-tone: #5c5c5c;
    --text-light: #fbfbfb;
  }
  * { margin: 0; padding: 0; box-sizing: border-box; }
  html, body {
    width: 1200px;
    height: 834px;
    overflow: hidden;
    background: var(--canvas);
  }
  .canvas {
    position: relative;
    width: 1200px;
    height: 834px;
  }
  .label {
    position: absolute;
    background: radial-gradient(ellipse at 50% 40%, var(--label-glow) 0%, var(--label-ink) 70%, var(--label-edge) 100%);
    color: var(--text-light);
    text-align: center;
    overflow: hidden;
  }
  .label--balm { left: 231px; top: 415px; width: 335px; height: 269px; }
  .label--serum { left: 630px; top: 332px; width: 339px; height: 290px; }

  .label .line {
    position: absolute;
    left: 0;
    width: 100%;
    line-height: 1;
    white-space: nowrap;
  }
  .brand-name { font-family: "Allura", cursive; }
  .product-type,
  .product-with,
  .product-ingredients,
  .product-volume,
  .brand-tagline { font-family: "Crimson Text", serif; }
  .brand-tagline { font-style: italic; letter-spacing: 0.04em; }

  .label--balm .brand-name { top: 86px; font-size: 34px; }
  .label--balm .product-type { top: 148px; font-size: 24px; }
  .label--balm .product-with { top: 178px; font-size: 13px; }
  .label--balm .product-ingredients { top: 195px; font-size: 14.5px; }
  .label--balm .brand-tagline { top: 222px; font-size: 11px; }
  .label--balm .product-volume { top: 244px; font-size: 10px; }

  .label--serum .brand-name { top: 104px; font-size: 44px; }
  .label--serum .product-type { top: 172px; font-size: 27px; }
  .label--serum .product-with { top: 204px; font-size: 14px; }
  .label--serum .product-ingredients { top: 224px; font-size: 16px; }
  .label--serum .brand-tagline { top: 252px; font-size: 12px; }
  .label--serum .product-volume { top: 272px; font-size: 10px; }

  .sprig {
    position: absolute;
    display: block;
  }
  .sprig--top-left { left: 10px; top: 12px; width: 48px; height: 40px; }
  .sprig--top-right { right: 4px; top: 6px; width: 44px; height: 78px; }
  .sprig--bottom-left { left: 0; bottom: 4px; width: 66px; height: 82px; }
</style>
</head>
<body>
<main class="canvas">

  <section class="label label--balm">
    <svg class="sprig sprig--top-left" role="img" aria-label="Fine-line botanical blossom illustration" viewBox="0 0 48 40">
      <rect width="48" height="40" rx="8" fill="var(--sprig-tone)" opacity="0.25"/>
    </svg>
    <svg class="sprig sprig--top-right" role="img" aria-label="Fine-line wild herb sprig illustration" viewBox="0 0 44 78">
      <rect width="44" height="78" rx="8" fill="var(--sprig-tone)" opacity="0.25"/>
    </svg>
    <svg class="sprig sprig--bottom-left" role="img" aria-label="Fine-line wildflower stems illustration" viewBox="0 0 66 82">
      <rect width="66" height="82" rx="8" fill="var(--sprig-tone)" opacity="0.25"/>
    </svg>
    <p class="line brand-name">Hollow Vesperine</p>
    <p class="line product-type">Facial Balm</p>
    <p class="line product-with">with</p>
    <p class="line product-ingredients">Sacred Tulsi &amp; Marshmallow Root</p>
    <p class="line brand-tagline">Crafted with Magic</p>
    <p class="line product-volume">50 ml</p>
  </section>

  <section class="label label--serum">
    <svg class="sprig sprig--top-left" role="img" aria-label="Fine-line botanical blossom illustration" viewBox="0 0 48 40">
      <rect width="48" height="40" rx="8" fill="var(--sprig-tone)" opacity="0.25"/>
    </svg>
    <svg class="sprig sprig--top-right" role="img" aria-label="Fine-line wild herb sprig illustration" viewBox="0 0 44 78">
      <rect width="44" height="78" rx="8" fill="var(--sprig-tone)" opacity="0.25"/>
    </svg>
    <svg class="sprig sprig--bottom-left" role="img" aria-label="Fine-line wildflower stems illustration" viewBox="0 0 66 82">
      <rect width="66" height="82" rx="8" fill="var(--sprig-tone)" opacity="0.25"/>
    </svg>
    <p class="line brand-name">Hollow Vesperine</p>
    <p class="line product-type">Body Serum</p>
    <p class="line product-with">with</p>
    <p class="line product-ingredients">Sweetgrass and Wild Mint</p>
    <p class="line brand-tagline">Crafted with Magic</p>
    <p class="line product-volume">120 ml</p>
  </section>

</main>
</body>
</html>
```